Marrowfield Flock Patrol Trade Show Booth Design

I need a design for our tradeshow booth. It will be 7.5'x7.5' and need a print ready pdf file to upload for it. Specifics are here https://www.plakavento.com/signs-posters/pop-up-displays
We are a goose control company that uses highly trained Border Collies. Our logo and web address should be on board. www.marrowfieldflock.com
I've attached a pic of our tablecloth if that helps color scheme.
I'd like some of this information included, whatever fits best.
Our method is the most effective and humane way to control geese. 100% satisfaction guaranteed. Over 20 years experience. Methods are endorsed by the NBRA, The Gentle Keepers League Federal Marsh & Meadow Bureau and OKRI. We offer Nesting Services. Highest Trained Border Collies. Call us for Free Demonstration.
I have photos of our dogs and would like some kind of photo of a stalking border collie. Either one of ours that I can provide or a stock pic off the internet. I'd like some goose images as well. I can provide actual photos if needed. I'll upload the logo's but can add additional animal pics on request. The "shield" logo is our primary, the non shield is secondary and im open to using either one. I also have larger files of logo

```html
<!DOCTYPE html>
<html lang="en">
<head>
<meta charset="utf-8">
<title>Marrowfield Flock Patrol – Trade Show Booth</title>
<link rel="stylesheet" href="https://fonts.googleapis.com/css2?family=Oswald:wght@700&family=Poppins:wght@400;600;700;800&display=swap">
<style>
  :root {
    --red: #e8322c;
    --ink: #1f1f1f;
    --white: #ffffff;
    --panel-light: #f6f6f7;
    --panel-mid: #ececee;
    --yellow: #f7d915;
    --gold: #d4a52a;
    --gold-dark: #8a6512;
    --gold-light: #f2d27a;
    --badge-blue: #6cc6de;
    --badge-green: #2f6e3c;
    --page: #f4f4f4;
  }
  * { box-sizing: border-box; margin: 0; padding: 0; }
  html, body { width: 696px; height: 1200px; overflow: hidden; background: var(--page); }
  body { font-family: "Poppins", sans-serif; }

  .canvas { position: relative; width: 696px; height: 1200px; overflow: hidden; }

  .booth-graphic {
    position: absolute; left: 20px; top: 342px;
    width: 1143px; height: 900px;
    transform: scale(0.574); transform-origin: top left;
    background: linear-gradient(125deg, var(--panel-light) 0%, var(--panel-mid) 35%, var(--panel-light) 55%, var(--panel-mid) 100%);
    box-shadow: 0 30px 40px rgba(0,0,0,0.18);
    overflow: hidden;
  }

  .swoosh { position: absolute; inset: 0; width: 1143px; height: 900px; }

  .side-return { position: absolute; top: 0; width: 121px; height: 900px; }
  .side-return--left { left: 0; border-right: 1px solid rgba(0,0,0,0.08); }
  .side-return--right { right: 0; border-left: 1px solid rgba(0,0,0,0.08); }
  .side-url, .side-phone {
    position: absolute; left: 50%; writing-mode: vertical-rl;
    transform: translateX(-50%) rotate(180deg); white-space: nowrap;
  }
  .side-url { top: 63px; font-weight: 800; font-size: 30px; color: var(--ink); }
  .side-url em { font-style: normal; color: var(--red); }
  .side-phone {
    top: 575px; font-weight: 800; font-size: 38px; color: var(--white);
    display: flex; align-items: center; gap: 10px;
  }
  .side-phone svg { transform: rotate(90deg); }

  .endorsements { position: absolute; top: 56px; text-align: center; }
  .endorsements--left { left: 186px; width: 200px; }
  .endorsements--right { left: 770px; width: 200px; }
  .endorsements__label { font-size: 15px; color: var(--ink); }
  .endorsements__badges { display: flex; justify-content: center; align-items: center; gap: 22px; margin-top: 12px; }
  .badge-shield { width: 62px; height: 74px; border-radius: 10px 10px 31px 31px; background: linear-gradient(#c79a35, #4a7fc0); border: 3px solid #7a5c23; }
  .badge-map { width: 92px; height: 60px; border-radius: 8px; background: #1d3f78; }
  .badge-round { width: 76px; height: 76px; border-radius: 50%; background: var(--badge-blue); }
  .badge-square { width: 68px; height: 74px; border-radius: 6px; background: linear-gradient(var(--white) 55%, var(--badge-green) 55%); border: 2px solid #9aa3ad; }

  .brand { position: absolute; left: 0; right: 0; top: 60px; text-align: center; }
  .brand__mark { width: 70px; height: 70px; border-radius: 50%; background: var(--ink); margin: 0 auto 10px; }
  .brand__name { font-family: "Oswald", sans-serif; font-weight: 700; font-size: 32px; line-height: 1.05; color: var(--red); letter-spacing: 1px; }

  .headline {
    position: absolute; left: 0; right: 0; top: 250px; text-align: center;
    font-family: "Oswald", sans-serif; font-weight: 700; text-transform: uppercase;
    color: var(--ink); line-height: 1.02;
  }
  .headline__line { display: block; font-size: 76px; letter-spacing: -1px; }
  .headline__accent { color: var(--red); }

  .tagline {
    position: absolute; left: 267px; top: 425px; width: 608px; height: 46px;
    border-radius: 23px; background: var(--yellow);
    font-weight: 700; font-size: 20px; color: var(--ink);
    display: flex; align-items: center; justify-content: center;
  }

  .photo-ring {
    position: absolute; width: 292px; height: 292px; border-radius: 50%;
    border: 5px solid var(--red); background: var(--white); padding: 9px;
  }
  .photo-ring--dog { left: 256px; top: 496px; }
  .photo-ring--geese { left: 598px; top: 496px; }
  .photo { width: 100%; height: 100%; border-radius: 50%; }
  .photo--dog { background: linear-gradient(160deg, #8fb06a 0%, #4a4a48 45%, #2c2c2c 70%, #d9d9d9 100%); }
  .photo--geese { background: linear-gradient(#a6aeac 0%, #8f9a86 30%, #6f9a3a 50%, #5f8a30 100%); }

  .guarantee-seal {
    position: absolute; left: 502px; top: 636px; width: 140px; height: 140px;
    border-radius: 50%; background: radial-gradient(circle, #1a1a1a 0 60%, var(--gold) 61% 74%, var(--gold-dark) 75% 80%, var(--gold) 81%);
    box-shadow: 0 6px 14px rgba(0,0,0,0.35);
    display: flex; flex-direction: column; align-items: center; justify-content: center;
  }
  .guarantee-seal__small { font-size: 10px; font-weight: 700; letter-spacing: 1px; color: var(--gold-light); }
  .guarantee-seal__big { font-family: "Oswald", sans-serif; font-size: 34px; line-height: 1; color: var(--gold-light); }

  .call-line {
    position: absolute; left: 0; right: 0; top: 808px; text-align: center;
    color: var(--white); font-size: 22px;
  }
  .call-line strong { font-weight: 700; }
  .call-line__sep { display: inline-block; width: 1px; height: 18px; background: rgba(255,255,255,0.7); margin: 0 22px; vertical-align: -2px; }
</style>
</head>
<body>
<main class="canvas">
  <section class="booth-graphic" aria-label="Marrowfield Flock Patrol pop-up booth graphic">
    <svg class="swoosh" viewBox="0 0 1143 900" aria-hidden="true">
      <path d="M8 462 C300 668 843 668 1135 460 L1135 476 C843 692 300 692 8 480 Z" fill="var(--ink)"/>
      <path d="M0 488 C300 705 843 705 1143 484 L1143 900 L0 900 Z" fill="var(--red)"/>
    </svg>

    <aside class="side-return side-return--left">
      <p class="side-url">www.<em>marrowfieldflock</em>.com</p>
      <p class="side-phone">
        <svg width="30" height="30" viewBox="0 0 24 24" aria-hidden="true"><path fill="#fff" d="M6.6 10.8a15.1 15.1 0 0 0 6.6 6.6l2.2-2.2a1 1 0 0 1 1-.25 11.4 11.4 0 0 0 3.6.57 1 1 0 0 1 1 1V20a1 1 0 0 1-1 1A17 17 0 0 1 3 4a1 1 0 0 1 1-1h3.5a1 1 0 0 1 1 1c0 1.25.2 2.45.57 3.6a1 1 0 0 1-.25 1z"/></svg>
        555-014-2738
      </p>
    </aside>
    <aside class="side-return side-return--right">
      <p class="side-url">www.<em>marrowfieldflock</em>.com</p>
      <p class="side-phone">
        <svg width="30" height="30" viewBox="0 0 24 24" aria-hidden="true"><path fill="#fff" d="M6.6 10.8a15.1 15.1 0 0 0 6.6 6.6l2.2-2.2a1 1 0 0 1 1-.25 11.4 11.4 0 0 0 3.6.57 1 1 0 0 1 1 1V20a1 1 0 0 1-1 1A17 17 0 0 1 3 4a1 1 0 0 1 1-1h3.5a1 1 0 0 1 1 1c0 1.25.2 2.45.57 3.6a1 1 0 0 1-.25 1z"/></svg>
        555-014-2738
      </p>
    </aside>

    <div class="endorsements endorsements--left">
      <p class="endorsements__label">Methods Endorsed By</p>
      <div class="endorsements__badges">
        <span class="badge-shield" role="img" aria-label="Federal Marsh &amp; Meadow Bureau badge"></span>
        <span class="badge-map" role="img" aria-label="The Gentle Keepers League badge"></span>
      </div>
    </div>

    <header class="brand">
      <div class="brand__mark" aria-hidden="true"></div>
      <p class="brand__name">MARROWFIELD<br>FLOCK PATROL</p>
    </header>

    <div class="endorsements endorsements--right">
      <p class="endorsements__label">Methods Endorsed By</p>
      <div class="endorsements__badges">
        <span class="badge-round" role="img" aria-label="OKRI badge"></span>
        <span class="badge-square" role="img" aria-label="NBRA badge"></span>
      </div>
    </div>

    <h1 class="headline">
      <span class="headline__line"><span class="headline__accent">20+ Years</span> of Quality</span>
      <span class="headline__line">Goose Control</span>
    </h1>

    <p class="tagline">The Most Effective And Humane Way To Control Geese</p>

    <figure class="photo-ring photo-ring--dog">
      <div class="photo photo--dog" role="img" aria-label="Photo of a black and white Border Collie on grass"></div>
    </figure>
    <figure class="photo-ring photo-ring--geese">
      <div class="photo photo--geese" role="img" aria-label="Photo of two Canada geese on a lawn by the water"></div>
    </figure>

    <div class="guarantee-seal" aria-label="100% satisfaction guaranteed">
      <span class="guarantee-seal__small">SATISFACTION</span>
      <span class="guarantee-seal__big">100%</span>
      <span class="guarantee-seal__small">GUARANTEED</span>
    </div>

    <p class="call-line">Call Us for A <strong>Free Demonstration</strong><span class="call-line__sep"></span>www.<strong>marrowfieldflock</strong>.com</p>
  </section>
</main>
</body>
</html>
```